Real Estate Business card design

Company Name: Thornbury Holdings, LLC
subtitle: We pay cash for houses!
Martin Calloway
Managing Director
518-674-2913
Mart@ThornburyHoldingsLLC.example
www.ThornburyHoldingsLLC.example

We pay referral fees for Seller and Buyer leads.

Back:
We offer referral fees for Seller and Buyer leads that close.

Please contact Ned at 518-674-2913 with your referrals or to learn more about the referral program!

I am open to different color options but I am going for a classic, elegant, clean, and professional look. Please use logo as a reference.

Target Market(s)

People selling their homes and people in the market for buying homes.

Contact Information for Business Card

please see project description

Font styles to use
Serif
Sans Serif
Script

Requirements
Must have
• must have my logo in it
Nice to have
• I like cards that are split down the middle but please come up with a few mock ups. Open to any color scheme.

```html
<!DOCTYPE html>
<html lang="en">
<head>
<meta charset="utf-8">
<title>Thornbury Holdings, LLC – Business Card</title>
<link rel="stylesheet" href="https://fonts.googleapis.com/css2?family=Libre+Baskerville:wght@400;700&family=Questrial&display=swap">
<style>
  :root {
    --navy: #464e5b;
    --navy-text: #3b4352;
    --gold: #c9a27a;
    --gold-soft: #d8b994;
    --white: #ffffff;
    --backdrop: #c4c4c4;
    --ink: #2f3540;
  }
  * { box-sizing: border-box; margin: 0; padding: 0; }
  html, body { width: 1200px; height: 788px; overflow: hidden; }
  body {
    background: var(--backdrop);
    font-family: "Questrial", sans-serif;
    display: flex; align-items: center; justify-content: center; gap: 30px;
  }
  .card {
    position: relative; width: 560px; height: 320px; border-radius: 18px;
    overflow: hidden; box-shadow: 0 10px 28px rgba(0,0,0,.22);
  }
  /* Front */
  .card-front { background: var(--white); }
  .card-front .wave { position: absolute; inset: 0; }
  .brand {
    position: absolute; left: 28px; top: 112px; width: 180px;
    display: flex; align-items: center; gap: 10px;
  }
  .brand-square { width: 14px; height: 14px; background: var(--gold); flex: none; }
  .brand-name {
    font-size: 21px; line-height: 1.15; color: var(--navy-text);
  }
  .divider {
    position: absolute; left: 222px; top: 46px; width: 1px; height: 170px;
    background: var(--gold-soft);
  }
  .contact { position: absolute; left: 240px; top: 34px; width: 300px; color: var(--ink); }
  .person-name {
    font-family: "Libre Baskerville", serif; font-size: 21px; letter-spacing: .5px;
    color: var(--navy-text); line-height: 1;
  }
  .person-name .surname { color: var(--gold); }
  .person-title { font-size: 13px; margin: 5px 0 12px; }
  .contact-line {
    display: flex; align-items: center; gap: 7px; font-size: 12.5px; margin-bottom: 6px;
  }
  .contact-line svg { width: 11px; height: 11px; flex: none; }
  .referral-note { font-size: 12.5px; line-height: 1.35; margin-top: 10px; }
  .tagline {
    position: absolute; right: 22px; bottom: 64px; color: var(--white);
    font-size: 13px; transform: rotate(-24deg); transform-origin: right bottom;
  }
  /* Back */
  .card-back {
    background: var(--navy); color: var(--white);
    display: flex; flex-direction: column; align-items: center; text-align: center;
  }
  .back-brand {
    margin-top: 60px; display: flex; align-items: center; gap: 12px;
  }
  .back-brand .brand-square { width: 20px; height: 20px; }
  .back-brand .brand-name { color: var(--gold); font-size: 28px; }
  .offer { margin-top: 40px; }
  .offer-headline { color: var(--gold); font-size: 22px; letter-spacing: .5px; }
  .offer-sub { font-size: 14px; margin-top: 3px; }
  .rule {
    width: 320px; height: 1px; margin: 12px 0;
    background: linear-gradient(90deg, transparent, var(--gold), transparent);
  }
  .contact-invite { font-size: 14px; line-height: 1.5; }
  .contact-invite .phone { color: var(--gold); font-size: 18px; }
</style>
</head>
<body>
  <article class="card card-front">
    <svg class="wave" viewBox="0 0 560 320" preserveAspectRatio="none" aria-hidden="true">
      <path d="M0,320 L0,306 C200,306 380,290 470,222 C510,192 530,176 560,171 L560,320 Z" fill="var(--navy)"/>
      <path d="M0,296 C200,296 375,280 463,212 C503,182 525,166 560,160" fill="none" stroke="var(--gold)" stroke-width="3"/>
    </svg>

    <div class="brand">
      <span class="brand-square"></span>
      <span class="brand-name">Thornbury Holdings, LLC</span>
    </div>

    <div class="divider"></div>

    <div class="contact">
      <h1 class="person-name">MARTIN <span class="surname">CALLOWAY</span></h1>
      <p class="person-title">Managing Director</p>
      <p class="contact-line">
        <svg viewBox="0 0 12 12"><path d="M2.5 1 4.5 1 5.3 3.5 4 4.5C4.7 6 6 7.3 7.5 8L8.5 6.7 11 7.5 11 9.5C11 10.3 10.3 11 9.5 11 5 11 1 7 1 2.5 1 1.7 1.7 1 2.5 1Z" fill="var(--gold)"/></svg>
        518-674-2913
      </p>
      <p class="contact-line">
        <svg viewBox="0 0 12 12"><rect x="0.5" y="2" width="11" height="8" fill="var(--gold)"/><path d="M0.5 2 6 6.5 11.5 2" fill="none" stroke="var(--white)" stroke-width="1"/></svg>
        Mart@ThornburyHoldingsLLC.example
      </p>
      <p class="contact-line">
        <svg viewBox="0 0 12 12"><circle cx="6" cy="6" r="5" fill="none" stroke="var(--gold)" stroke-width="1.4"/><path d="M1 6H11M6 1C4 3.5 4 8.5 6 11M6 1C8 3.5 8 8.5 6 11" fill="none" stroke="var(--gold)" stroke-width="1"/></svg>
        www.ThornburyHoldingsLLC.example
      </p>
      <p class="referral-note">We pay referral fees<br>for Seller and Buyer leads.</p>
    </div>

    <p class="tagline">We pay cash for houses!</p>
  </article>

  <article class="card card-back">
    <div class="back-brand">
      <span class="brand-square"></span>
      <span class="brand-name">Thornbury Holdings, LLC</span>
    </div>
    <div class="offer">
      <p class="offer-headline">We offer referral fees</p>
      <p class="offer-sub">for Seller and Buyer leads that close.</p>
    </div>
    <div class="rule"></div>
    <p class="contact-invite">
      Please contact Ned at <span class="phone">518-674-2913</span><br>
      with your referrals or to learn more about the referral program!
    </p>
  </article>
</body>
</html>
```